Can you make FairlyKind look better than average? We need business cards and a logo refresh :-)

REVISED BRIEF

PRIORITY

VECTOR LOGO

Create a vector version of our existing logo. The logo must not change from its current design, weight or font.

Deliverables

- Logo in blue (#2540BB)
- Logo in white (#FFFFFF)
- Logo in grey (#36454F)
- All logos on transparent background
- All logos in PNG & SVG formats. (SVG must NOT distort stroke width when resized)

BRAND MARK

Create a brand mark for use with the logo. This should be possible to used with the logo and on its own as a stand alone graphical device that represents the FAIRLYKIND brand.

https://sitecrafter.example.com/resources/glossary/what-is-a-brand-mark

Deliverables

- Brand Mark in blue (#2540BB)
- Brand Mark in white (#FFFFFF)
- Brand Mark in grey (#36454F)
- Brand Mark on transparent background
- Brand Mark in PNG & SVG formats. (SVG must NOT distort stroke width when resized)
- Logo combined with Brand Mark (colours and formats)
.

Business Card Layout

Create 2 layouts with the following details:-

Marcus Trent
Co-Founder & Chief Product Officer

marcus@fairlykind.example.nz
www.fairlykind.example.nz
0279816354

Callum Bryce
Founder & CEO

hello@fairlykind.example.nz
www.fairlykind.example.nz
021 948 6207

DESIGN CONSIDERATIONS

Create versions with ‘Shaping Names With Heart’ tag line incorporated within the design and without (maintain separation of logo from tag line)

- Create a version with and without the brand mark
- Keep it clean and simple but elevate the design with subtle design effects
- Consider use of raised spot gloss colour (this can be white on white for subtle or blue on blue or blue on white)
- Consider use of spot gloss colour (this can be white on white for subtle or blue on blue or blue on white)
- Consider use of letterpress indentation
- Ensure contact details are legible, use sans-serif font

PREVIOUS BRIEF

We need a business card design for our business FairlyKind. We are a purpose driven brand and media agency that helps brands and charities plan and buy traditional media campaigns (TV, Radio, Print, Outdoor etc). We give a significant amount of the media booking fees we receive from media vendors to charity in the name of our clients. https://www.socialnet.example.com/posts/wearefairlykind_giveback-fairlykind-shapingnameswithheart-activity-5820394716253849102-Xqzt

Our strapline is 'Shaping Names With Heart'.

We want to keep our logo design as it is but it does need tightening up and made into a proper vector image as it's been created from a font.

Our brand colour is #2540BB and we need to keep this.

Our brand is professional but human, warm and engaging and doesn't take itself too seriously.

Things We Need
- vectorisation and tidying up of existing logo
- We'd like you to think about how we can incorporate a brand mark with the logo to add another dimension to our brand
- business card layout and design
- we'll be using cardloop.example.com to print the cards so please take a look at the options they have (spot gloss, foil, letterpress, square cards and even the backs of the cards can have a different design on every single card!
- potential opportunity for different famous quotes on the back or imagery or slight design differences
- we'd be open to the use of an emoji or emojiis as the brandmark or to be incorporated into the card designs
- we can have as many different design batches as we like for the backs of the cards

https://www.cardloop.example.com/au/business-cards

We want to make an impact, we want to be seen as professional but fun, we want to be different.

Here's a press release of what we're about.

https://adwirenews.example.co.nz/movings-shakings/fairlykind-welcomes-marcus-trent-as-co-founder/

Be bold, be different, there is no such thing as a bad idea. We're open to anything so please bring your best ideas and have fun with it! Go crazy if you like!
____________
Marcus Trent
marcus@fairlykind.example.nz
0279816354

Callum Bryce
Founder & CEO
hello@fairlykind.example.nz
021 948 6207

Shaping Names With Heart

________

These are the only details we MUST have on the cards, the rest is up to you. Just make sure you use all of your creativity but don't feel the need to crowd the card with too much, let it breathe as well.

In terms of font for the details, we'll leave that up to you, just ensure it's legible. Oh and please don't take any design inspiration from our website - that will be changing!

Please don't let the design and layout look cheap and tacky though. It needs to still feel premium but personable.

Thanks

Marcus
Updates

Many designs are changing the logo and this was NOT in the brief. We need a brand mark to complement the logo. We need to see the logo with and without the brand mark. We need to see the business card with both logo + brand mark and logo on its own We need to see the business card with and without the tagline 'Shaping Names With Heart'

Industry/Entity Type

purpose driven Brand & Media Agency

Contact Information for Business Card

Shaping Names With Heart
Marcus Trent, Co-Founder & Chief Product Officer, marcus@fairlykind.example.nz fairlykimd.example.nz, 0279 816 354

Callum Bryce, Founder & CEO hello@fairlykind.example.nz, fairlykimd.example.nz, 021 948 6207

Font styles to use
Serif
Sans Serif

Colors
0054AA
0677BA
7BADD7
CADEEF
E8F1F8

Requirements
Must have
• brand mark, vector version of existing logo, Shaping Names With Heart tagline, existing logo traced and vectorised. Must fully explore the design options from cardloop.example.com that can enhance the overall card design
Nice to have
• brandmark to help elevate the logo, maybe incorporate some other design elements into the card like lines, or grids.
Should not have
• A cheap look and feel

```html
<!DOCTYPE html>
<html lang="en">
<head>
<meta charset="utf-8">
<title>FairlyKind business cards</title>
<link rel="stylesheet" href="https://fonts.googleapis.com/css2?family=Besley:wght@600;800&family=Inter:wght@500;600&display=swap">
<style>
  :root {
    --page: #eeeeef;
    --card-blue: #2540bb;
    --tone-blue: #1e339a;
    --ink-light: #e4e7f2;
    --card-edge: #172a86;
    --serif: "Besley", Georgia, serif;
    --sans: "Inter", Arial, sans-serif;
  }
  * { margin: 0; padding: 0; box-sizing: border-box; }
  html, body { width: 1200px; height: 800px; overflow: hidden; background: var(--page); }
  .sheet {
    width: 1200px; height: 800px;
    display: flex; align-items: center; justify-content: center; gap: 60px;
  }
  .card {
    position: relative;
    width: 520px; height: 330px;
    background: var(--card-blue);
    border-bottom: 3px solid var(--card-edge);
    box-shadow: 0 10px 24px rgba(20, 30, 80, 0.18);
    overflow: hidden;
  }

  /* Contact side */
  .tagline-stack {
    position: absolute; top: 20px; left: 292px;
    color: var(--tone-blue);
    font-family: var(--serif);
    font-weight: 800; font-size: 38px; line-height: 1;
    letter-spacing: -0.5px;
  }
  .tagline-stack span { display: block; }
  .tagline-stack span:nth-child(2) { padding-left: 22px; }
  .tagline-stack span:nth-child(3) { padding-left: 92px; }
  .tagline-stack span:nth-child(4) { padding-left: 72px; }
  .contacts {
    position: absolute; left: 32px; bottom: 26px;
    color: var(--ink-light);
    font-family: var(--sans);
    font-weight: 500; font-size: 12.5px; line-height: 1.38;
  }
  .contact + .contact { margin-top: 12px; }
  .contact p { white-space: nowrap; }
  .contact .person { font-weight: 600; }

  /* Logo side */
  .brand {
    position: absolute; left: 0; right: 0; top: 122px;
    display: flex; flex-direction: column; align-items: center;
  }
  .brand-lockup { display: flex; align-items: center; gap: 14px; }
  .brand-mark {
    width: 26px; height: 26px; border-radius: 50%;
    background: var(--ink-light);
  }
  .brand-name {
    color: var(--ink-light);
    font-family: var(--serif);
    font-weight: 800; font-size: 48px; line-height: 1;
    letter-spacing: -1px;
  }
  .brand-tagline {
    align-self: flex-end; margin-right: 52px; margin-top: 12px;
    color: var(--tone-blue);
    font-family: var(--serif);
    font-weight: 600; font-size: 15px;
  }
</style>
</head>
<body>
  <main class="sheet">
    <section class="card card-back" aria-label="Business card, contact side">
      <div class="tagline-stack" aria-label="Shaping Names With Heart">
        <span>Shaping</span>
        <span>Names</span>
        <span>With</span>
        <span>Heart</span>
      </div>
      <div class="contacts">
        <div class="contact">
          <p class="person">Marcus Trent</p>
          <p>Co-Founder &amp; Chief Product Officer</p>
          <p>marcus@fairlykind.example.nz</p>
          <p>www.fairlykind.example.nz</p>
          <p>0279816354</p>
        </div>
        <div class="contact">
          <p class="person">Callum Bryce</p>
          <p>Founder &amp; CEO</p>
          <p>hello@fairlykind.example.nz</p>
          <p>www.fairlykind.example.nz</p>
          <p>021 948 6207</p>
        </div>
      </div>
    </section>

    <section class="card card-front" aria-label="Business card, logo side">
      <div class="brand">
        <div class="brand-lockup">
          <span class="brand-mark" aria-hidden="true"></span>
          <h1 class="brand-name">FAIRLYKIND.</h1>
        </div>
        <p class="brand-tagline">Shaping Names With Heart</p>
      </div>
    </section>
  </main>
</body>
</html>
```